ridgeway diner & grill

menu design contracting menu to two views. reducing number of offerings. website. http://ridgewaydiner-harborvale.com/ridgewaymenu.html
have reduced our menu offering by 25 items to achieve a 2 view profile vs our current 5 view look. 8 1/2 x 11 preferred but 8 1/2 by 14 possible. Would like to employ a menu board concept but sleeves will also be a considered option.

Target Market(s)

families, blue collar, home style, meat loaf, fried chicken, burgers, chicken fried steak etc

Industry/Entity Type

American Restaurant

Font styles to use
Sans Serif

Colors
f68e4d
faa54b
fece3e
fbee3e
aaaaaa
9d9d9d
b1b1b1
1b1b1b

Requirements
Must have
• 2 views
Nice to have
• colors
Should not have
• clutter, unstructured,

```html
<!DOCTYPE html>
<html lang="en">
<head>
<meta charset="utf-8">
<title>Ridgeway Diner &amp; Grill – Country Homestyle Favorites</title>
<link href="https://fonts.googleapis.com/css2?family=Old+Standard+TT:wght@700&family=Roboto+Condensed:wght@400;700&display=swap" rel="stylesheet">
<style>
  :root {
    --paper-light: #f1e4c8;
    --paper-mid: #e6d3ae;
    --paper-edge: #cfb588;
    --menu-red: #b5262a;
    --ink: #2e2118;
    --rule: #b8473f;
    --art-bread: #d9a766;
    --art-fill: #c8865a;
  }
  * { margin: 0; padding: 0; box-sizing: border-box; }
  html, body { width: 928px; height: 1200px; overflow: hidden; }
  body {
    font-family: "Roboto Condensed", "Arial Narrow", sans-serif;
    color: var(--ink);
    background: var(--paper-mid);
  }
  .menu-page {
    position: relative;
    width: 928px;
    height: 1200px;
    background: radial-gradient(ellipse at 50% 40%, var(--paper-light) 0%, var(--paper-mid) 65%, var(--paper-edge) 100%);
    overflow: hidden;
  }
  .brand {
    position: absolute;
    top: 52px; left: 0; width: 100%;
    text-align: center;
  }
  .brand-name {
    font-family: "Roboto Condensed", sans-serif;
    font-weight: 700;
    font-size: 38px;
    color: var(--menu-red);
    letter-spacing: 1px;
    text-transform: lowercase;
  }
  .page-title {
    position: absolute;
    top: 170px; left: 0; width: 100%;
    text-align: center;
    font-family: "Old Standard TT", serif;
    font-weight: 700;
    font-size: 35px;
    letter-spacing: 3px;
    color: var(--menu-red);
  }
  .section-divider {
    position: absolute;
    left: 0; width: 928px; height: 48px;
  }
  .section-divider .rule {
    position: absolute;
    top: 23px; height: 1.5px;
    background: var(--rule);
  }
  .section-divider .rule.left { left: 20px; width: 400px; }
  .section-divider .rule.right { left: 508px; width: 400px; }
  .section-divider .icon-slot {
    position: absolute;
    left: 434px; top: 2px;
    width: 60px; height: 44px;
  }
  .menu-column {
    position: absolute;
    width: 390px;
  }
  .menu-item { margin-bottom: 18px; }
  .item-head {
    display: flex;
    justify-content: space-between;
    color: var(--menu-red);
    font-weight: 700;
    font-size: 17px;
    line-height: 19px;
    text-transform: uppercase;
  }
  .item-head .item-name { max-width: 300px; }
  .item-price { font-weight: 400; }
  .item-desc {
    font-size: 13.4px;
    line-height: 16px;
    text-transform: uppercase;
    letter-spacing: 0.1px;
  }
  .col-left { left: 58px; }
  .col-right { left: 480px; }
  .feature-art {
    position: absolute;
    left: 40px; top: 985px;
    width: 860px; height: 172px;
  }
  .advisory {
    position: absolute;
    left: 0; top: 1161px; width: 100%;
    text-align: center;
    font-size: 11px;
    line-height: 13px;
    text-transform: uppercase;
    color: var(--ink);
  }
</style>
</head>
<body>
<main class="menu-page">

  <header class="brand">
    <span class="brand-name">ridgeway diner &amp; grill</span>
  </header>

  <h1 class="page-title">COUNTRY HOMESTYLE FAVORITES</h1>

  <!-- Poultry section -->
  <div class="section-divider" style="top:232px">
    <span class="rule left"></span><span class="rule right"></span>
    <svg class="icon-slot" viewBox="0 0 60 44" role="img" aria-label="Roast poultry on a platter icon">
      <rect x="4" y="6" width="52" height="34" rx="12" fill="var(--menu-red)"/>
    </svg>
  </div>

  <section class="menu-column col-left" style="top:302px">
    <div class="menu-item">
      <div class="item-head"><span class="item-name">Homemade Fried Chicken Dinner</span><span class="item-price">$10.99</span></div>
      <p class="item-desc">Hand breaded breast, thigh, leg or wing served with mashed potatoes, country gravy, vegetable of the day &amp; house baked bread! (small portion 8.99)</p>
    </div>
    <div class="menu-item">
      <div class="item-head"><span class="item-name">Turkey and Dressing Dinner</span><span class="item-price">$9.99</span></div>
      <p class="item-desc">Slow roasted turkey served with dressing, mashed potatoes, turkey gravy, vegetable of the day &amp; house baked bread! (small portion 8.99)</p>
    </div>
    <div class="menu-item">
      <div class="item-head"><span class="item-name">Chicken Fried Chicken Special</span><span class="item-price">$10.99</span></div>
      <p class="item-desc">Hand breaded chicken breast served with corn on the cob, mashed potatoes, country gravy &amp; house baked bread</p>
    </div>
  </section>

  <section class="menu-column col-right" style="top:302px">
    <div class="menu-item">
      <div class="item-head"><span class="item-name">Char-Broiled Chicken Breast</span><span class="item-price">$11.99</span></div>
      <p class="item-desc">10 oz. breast served with choice of potato &amp; house baked bread!</p>
    </div>
    <div class="menu-item">
      <div class="item-head"><span class="item-name">Hand Breaded Chicken Strips</span><span class="item-price">$7.99</span></div>
      <p class="item-desc">We bread them ourselves, served with choice of potato &amp; house baked bread! (small portion 6.99)</p>
    </div>
  </section>

  <!-- Beef section -->
  <div class="section-divider" style="top:534px">
    <span class="rule left"></span><span class="rule right"></span>
    <svg class="icon-slot" viewBox="0 0 60 44" role="img" aria-label="Roast meat on a platter icon">
      <rect x="4" y="6" width="52" height="34" rx="12" fill="var(--menu-red)"/>
    </svg>
  </div>

  <section class="menu-column col-left" style="top:600px">
    <div class="menu-item">
      <div class="item-head"><span class="item-name">Good Ol' Liver &amp; Onions</span><span class="item-price">$8.99</span></div>
      <p class="item-desc">Beef liver, pan fried, topped with beef gravy &amp; grilled onions, served with mashed potatoes, vegetable of the day &amp; house baked bread! (small portion 7.99)</p>
    </div>
    <div class="menu-item">
      <div class="item-head"><span class="item-name">Old Fashioned Hot Roast Beef Sandwich</span><span class="item-price">$9.99</span></div>
      <p class="item-desc">Our famous roast beef served open face over mashed potatoes, country thick white bread &amp; beef gravy (small portion 8.99)</p>
    </div>
  </section>

  <section class="menu-column col-right" style="top:600px">
    <div class="menu-item">
      <div class="item-head"><span class="item-name">Old Fashioned Meatloaf Dinner</span><span class="item-price">$8.99</span></div>
      <p class="item-desc">House made loaf served with mashed potatoes, beef gravy, vegetable of the day and house baked bread! (small portion 7.99)</p>
    </div>
    <div class="menu-item">
      <div class="item-head"><span class="item-name">Roast Beef Dinner!</span><span class="item-price">$10.99</span></div>
      <p class="item-desc">Our famous roast beef, served with mashed potatoes, beef gravy, vegetable of the day &amp; our house baked bread (small portion 8.99)</p>
    </div>
  </section>

  <!-- Seafood section -->
  <div class="section-divider" style="top:796px">
    <span class="rule left"></span><span class="rule right"></span>
    <svg class="icon-slot" viewBox="0 0 60 44" role="img" aria-label="Fish on a platter icon">
      <rect x="4" y="6" width="52" height="34" rx="12" fill="var(--menu-red)"/>
    </svg>
  </div>

  <section class="menu-column col-left" style="top:862px">
    <div class="menu-item">
      <div class="item-head"><span class="item-name">Atlantic Salmon Fillet!</span><span class="item-price">$12.99</span></div>
      <p class="item-desc">8 oz. fillet, charbroiled &amp; topped with a sweet bourbon glaze, served with choice of potato &amp; house baked bread</p>
    </div>
    <div class="menu-item">
      <div class="item-head"><span class="item-name">Fried Shrimp Basket</span><span class="item-price">$10.99</span></div>
      <p class="item-desc">One full pound of deep fried shrimp with bottleneck french fries! (small portion 8.99)</p>
    </div>
  </section>

  <section class="menu-column col-right" style="top:862px">
    <div class="menu-item">
      <div class="item-head"><span class="item-name">Country Fried Catfish</span><span class="item-price">$10.99</span></div>
      <p class="item-desc">Hand breaded catfish fillets, served with choice of potato &amp; house baked bread!</p>
    </div>
    <div class="menu-item">
      <div class="item-head"><span class="item-name">Chicken Strip &amp; Fried Shrimp</span><span class="item-price">$9.99</span></div>
      <p class="item-desc">Two of our hand breaded chicken strips &amp; half pound of fried shrimp with bottleneck french fries!</p>
    </div>
  </section>

  <svg class="feature-art" viewBox="0 0 860 172" preserveAspectRatio="none" role="img" aria-label="Drawn illustration of a deli sandwich, fresh vegetables and a loaded sub roll">
    <defs>
      <linearGradient id="artTone" x1="0" y1="0" x2="1" y2="0">
        <stop offset="0" stop-color="var(--art-bread)" stop-opacity="0.75"/>
        <stop offset="0.5" stop-color="var(--art-fill)" stop-opacity="0.35"/>
        <stop offset="1" stop-color="var(--art-bread)" stop-opacity="0.8"/>
      </linearGradient>
    </defs>
    <rect x="0" y="0" width="860" height="172" rx="30" fill="url(#artTone)"/>
  </svg>

  <footer class="advisory">
    Consumer advisory: consuming raw or undercooked meat, poultry, seafood, shellfish or eggs may increase your risk of foodborne illness.<br>
    Sorry, we can't split small portions. Split order will be charged small portion price or 1/2 price plus $1 per person if small portion not offered.
  </footer>

</main>
</body>
</html>
```